Powepoint Templates From Logo

We need 3 Powerpoint templates for use in a variety of presentations we develop and customize. Primary uses of the powerpoint presentations are for printed "pitch books" describing our firm's capabilities and approach (a lot of words with some design elements that we have developed), printed presentations of the results of financial evaluations of our clients (lots of charts and graphs) and as the talking points for speeches.

The design needs to be professional and "solid" to establish that we are capable of selling your multi-million dollar business, but also be a little different to show that we are not just boring MBA's.

Our current website and other materials have been developed internally and leave a great deal to be desired. I have initiated this project to demonstrate how much our look can be improved and, if successful, I hope to do much bigger projects in the future.
Updates

This is my first project and I thaank you all for your participation. Since I am new to this, I don;t know if I am providing the help and feedback as I should. Please feel free to let me know how I can be a better customer.

Target Market(s)

professionals (lawyers, accountaants), business owners, business groups, technology people

Industry/Entity Type

Financial

Requirements
Must have
• our logo
a place where logo of client can be inserted if appropriate
templates for the following pages
title page
standard bullet narrative page
page for charts and graphs to mostly fill the page
Should not have a lot of dark solid color that has to be printed.

Nice to have
• something to perk up the color a little

```html
<!DOCTYPE html>
<html lang="en">
<head>
<meta charset="utf-8">
<title>Index</title>
<link href="https://fonts.googleapis.com/css2?family=PT+Sans:wght@400;700&display=swap" rel="stylesheet">
<style>
  :root {
    --navy: #1f3566;
    --text-grey: #6a6a6a;
    --rule-grey: #8a8d92;
    --white: #ffffff;
    --bg-centre: #ffffff;
    --bg-edge: #dfe0e2;
  }
  * { margin: 0; padding: 0; box-sizing: border-box; }
  html, body { width: 1200px; height: 900px; overflow: hidden; }
  body { font-family: "PT Sans", "Segoe UI", sans-serif; background: var(--white); }

  .slide {
    position: relative;
    width: 1200px;
    height: 900px;
    background: radial-gradient(ellipse 60% 60% at 50% 38%, var(--bg-centre) 0%, var(--bg-edge) 100%);
    overflow: hidden;
  }

  .header {
    position: absolute;
    left: 0; top: 0;
    width: 1200px; height: 119px;
    background: var(--white);
  }
  .header-band {
    position: absolute;
    left: 0; top: 119px;
    width: 1200px; height: 10px;
    background: var(--navy);
  }

  .firm-name {
    position: absolute;
    left: 26px; top: 46px;
    font-size: 24px;
    font-weight: 400;
    color: var(--navy);
    line-height: 1;
  }
  .firm-note {
    position: absolute;
    left: 26px; top: 78px;
    font-size: 12px;
    font-weight: 400;
    color: var(--text-grey);
    line-height: 1;
  }

  .client-name {
    position: absolute;
    right: 30px; top: 62px;
    font-size: 22px;
    font-weight: 400;
    color: var(--text-grey);
    line-height: 1;
  }

  .index {
    position: absolute;
    left: 236px; top: 0;
    width: 800px;
  }
  .index-title {
    position: absolute;
    left: 0; top: 242px;
    font-size: 38px;
    font-weight: 400;
    color: var(--navy);
    line-height: 1;
  }
  .rule {
    position: absolute;
    left: 0;
    width: 770px;
    height: 1px;
    background: var(--rule-grey);
  }
  .rule::after {
    content: "";
    position: absolute;
    right: -6px; top: -7px;
    width: 13px; height: 13px;
    border-radius: 2px;
    background: var(--navy);
  }
  .rule-top { top: 278px; }
  .rule-bottom { top: 682px; }

  .index-list { list-style: none; }
  .index-item {
    position: absolute;
    left: 1px;
    display: flex;
    align-items: center;
    gap: 18px;
    font-size: 30px;
    color: var(--text-grey);
    line-height: 1;
  }
  .index-item::before {
    content: "";
    width: 26px; height: 26px;
    background: var(--navy);
    border: 2px solid var(--white);
    border-radius: 3px;
    box-shadow: 0 0 2px rgba(0,0,0,0.25);
  }
  .index-item:nth-child(1) { top: 336px; }
  .index-item:nth-child(2) { top: 407px; }
  .index-item:nth-child(3) { top: 478px; }
  .index-item:nth-child(4) { top: 549px; }
  .index-item:nth-child(5) { top: 620px; }

  .footer-band {
    position: absolute;
    left: 0; bottom: 0;
    width: 1200px; height: 8px;
    background: var(--navy);
  }
  .page-corner {
    position: absolute;
    left: 0; bottom: 0;
  }
  .page-number {
    position: absolute;
    left: 10px; bottom: 8px;
    font-size: 28px;
    color: var(--white);
    line-height: 1;
  }
</style>
</head>
<body>
  <main class="slide">
    <header class="header">
      <div class="firm-name">Harbourline Partners</div>
      <div class="firm-note">Corporate finance counsel</div>
      <div class="client-name">Client Name</div>
    </header>
    <div class="header-band"></div>

    <section class="index">
      <h1 class="index-title">Index</h1>
      <div class="rule rule-top"></div>
      <ul class="index-list">
        <li class="index-item">Introduction</li>
        <li class="index-item">Runthrough</li>
        <li class="index-item">Benchmarking</li>
        <li class="index-item">Marketing</li>
        <li class="index-item">Exit strategy</li>
      </ul>
      <div class="rule rule-bottom"></div>
    </section>

    <svg class="page-corner" width="80" height="84" viewBox="0 0 80 84">
      <polygon points="0,0 78,84 0,84" fill="var(--navy)"/>
    </svg>
    <div class="page-number">2.</div>
    <div class="footer-band"></div>
  </main>
</body>
</html>
```